Business Card Design

We need a business card design for a consulting firm which provides safety and risk management consulting services for public venues, hotels and tourist attractions. The business card design should include the attached logo unedited with a design based on incorporating the existing logo with a design of geometric patterns or lines on a predominantly white background.

Industry/Entity Type

Business

Contact Information for Business Card

Dane Morvello
Director & Principal Consultant

Ph: +61 (0) 468502 174
PO Box 456 Kellmore Vale, NSW Australia 2563
info@corvanwellandcare.com

(back of card to include website www.corvanwellandcare.com

```html
<!DOCTYPE html>
<html lang="en">
<head>
<meta charset="UTF-8">
<title>Corvan Welland Care – Business Card</title>
<link href="https://fonts.googleapis.com/css2?family=Open+Sans:wght@400;600&display=swap" rel="stylesheet">
<style>
  :root {
    --backdrop: #3b3634;
    --card: #ffffff;
    --brand-blue: #2a93d8;
    --brand-green: #6cbf3c;
    --ink: #1b1b1b;
    --rule: #2a93d8;
  }
  * { margin: 0; padding: 0; box-sizing: border-box; }
  html, body {
    width: 1200px;
    height: 844px;
    overflow: hidden;
    background: var(--backdrop);
    font-family: "Open Sans", Arial, sans-serif;
  }
  .stage {
    position: relative;
    width: 1200px;
    height: 844px;
  }
  .card {
    position: absolute;
    top: 263px;
    width: 520px;
    height: 318px;
    background: var(--card);
    overflow: hidden;
    box-shadow: 0 10px 30px rgba(0,0,0,.35);
  }

  /* Contact side */
  .card--contact { left: 50px; }
  .card--contact .band {
    position: absolute;
    left: 0; right: 0;
    height: 14px;
    background: var(--brand-blue);
  }
  .card--contact .band--top { top: 0; }
  .card--contact .band--bottom { bottom: 0; }
  .identity {
    position: absolute;
    top: 58px;
    left: 0; right: 0;
    text-align: center;
  }
  .identity__name {
    display: inline-block;
    color: var(--brand-blue);
    font-weight: 600;
    font-size: 22px;
    letter-spacing: .5px;
    text-transform: uppercase;
    padding: 0 14px 4px;
    border-bottom: 2px solid var(--rule);
  }
  .identity__title {
    margin-top: 6px;
    font-size: 15px;
    color: var(--ink);
  }
  .contact-list {
    position: absolute;
    top: 164px;
    left: 0; right: 0;
    list-style: none;
    text-align: center;
    color: var(--ink);
    font-size: 15px;
    line-height: 30px;
  }

  /* Brand side */
  .card--brand { left: 630px; }
  .accent {
    position: absolute;
    width: 22px;
    height: 52px;
    background: var(--brand-blue);
    border-right: 4px solid var(--brand-green);
  }
  .accent--top { top: 40px; right: 0; border-right: none; border-left: 4px solid var(--brand-green); }
  .accent--side { top: 150px; left: 0; }
  .brand {
    position: absolute;
    top: 118px;
    left: 0; right: 0;
    display: flex;
    align-items: center;
    justify-content: center;
    gap: 12px;
  }
  .brand__dot {
    width: 18px;
    height: 18px;
    border-radius: 50%;
    background: var(--brand-blue);
  }
  .brand__name {
    font-size: 30px;
    font-weight: 600;
    color: var(--brand-blue);
    letter-spacing: .5px;
  }
  .website {
    position: absolute;
    top: 214px;
    left: 0; right: 0;
    text-align: center;
    font-size: 14px;
    color: var(--ink);
  }
</style>
</head>
<body>
<main class="stage">
  <section class="card card--contact" aria-label="Business card, contact side">
    <div class="band band--top"></div>
    <div class="identity">
      <h1 class="identity__name">Dane Morvello</h1>
      <p class="identity__title">Director &amp; Principal Consultant</p>
    </div>
    <ul class="contact-list">
      <li>+61 (0) 468502 174</li>
      <li>info@corvanwellandcare.com</li>
      <li>PO Box 456 Kellmore Vale, NSW Australia 2563</li>
    </ul>
    <div class="band band--bottom"></div>
  </section>

  <section class="card card--brand" aria-label="Business card, brand side">
    <div class="accent accent--top"></div>
    <div class="accent accent--side"></div>
    <div class="brand">
      <span class="brand__dot"></span>
      <span class="brand__name">Corvan Welland Care</span>
    </div>
    <p class="website">www.corvanwellandcare.com</p>
  </section>
</main>
</body>
</html>
```